rk ironcraft business card metallic look

revamp the existing design but want card to have a metalic look to it

Target Market(s)

construction industry

Industry/Entity Type

constrction

Contact Information for Business Card

front of card RK Ironcraft, phone 4165550193, email rk.ironcraftt@veltrano.com and instagram account; rk_ironcraft_

Font styles to use
Other font styles liked:
• masculine

Colors

Designer to choose only greyscale colors for use in the design.

Requirements
Must have
• back side RK Ironcraft then a list of everything : Siding, ACM Panels, Standing Seam,Soffit, Fascia, Gutters,Metal,Alu,inum, Viynyl, Metal Roofs and roof repairs
Nice to have
• I would like to keep the look of the existing card with the metal grids on the front
Should not have
• Need a design in two days

```html
<!DOCTYPE html>
<html lang="en">
<head>
<meta charset="utf-8">
<title>RK Ironcraft Business Card</title>
<link rel="stylesheet" href="https://fonts.googleapis.com/css2?family=Montserrat:ital,wght@0,400;0,700;0,800;1,400&display=swap">
<style>
  :root {
    --canvas: #585858;
    --front-dark: #1b1b1b;
    --front-mid: #2e2e2e;
    --front-band: #262626;
    --steel-light: #c9cbce;
    --steel-mid: #8d9094;
    --steel-dark: #3f4246;
    --back-light: #f4f4f4;
    --back-mid: #dcdcdc;
    --ink-dark: #151515;
    --ink-light: #ececec;
    --icon-fill: #d6d6d6;
  }
  * { margin: 0; padding: 0; box-sizing: border-box; }
  html, body { width: 1200px; height: 1200px; overflow: hidden; }
  body {
    background: var(--canvas);
    font-family: "Montserrat", sans-serif;
    position: relative;
  }
  .card {
    position: absolute;
    left: 294px;
    width: 612px;
    height: 382px;
    overflow: hidden;
    box-shadow: 6px 8px 14px rgba(0,0,0,0.35);
  }
  .card-front {
    top: 199px;
    background:
      linear-gradient(160deg, transparent 62%, var(--front-band) 62%),
      linear-gradient(135deg, var(--front-mid) 0%, var(--front-dark) 55%, var(--front-mid) 100%);
  }
  .card-back {
    top: 619px;
    background: linear-gradient(150deg, var(--back-mid) 0%, var(--back-light) 45%, var(--back-mid) 100%);
  }
  .steel-panel {
    position: absolute;
    inset: 0;
    width: 612px;
    height: 382px;
  }
  .front-name {
    position: absolute;
    left: 46px;
    top: 64px;
    font-weight: 800;
    font-size: 46px;
    line-height: 1.0;
    letter-spacing: 1px;
    text-transform: uppercase;
    color: var(--steel-light);
  }
  .contact-list {
    position: absolute;
    left: 46px;
    top: 214px;
    list-style: none;
  }
  .contact-item {
    display: flex;
    align-items: center;
    height: 39px;
    color: var(--ink-light);
    font-size: 21px;
    font-weight: 400;
    letter-spacing: 0.6px;
  }
  .contact-item.phone { font-weight: 700; font-size: 24px; letter-spacing: 1px; }
  .contact-icon {
    width: 32px;
    height: 32px;
    margin-right: 16px;
    flex: none;
  }
  .back-name {
    position: absolute;
    left: 0;
    right: 0;
    top: 92px;
    text-align: center;
    font-weight: 800;
    font-size: 52px;
    line-height: 1.0;
    letter-spacing: 1px;
    text-transform: uppercase;
    color: var(--ink-dark);
  }
  .service-list {
    position: absolute;
    left: 0;
    right: 0;
    top: 233px;
    text-align: center;
    font-style: italic;
    font-weight: 400;
    font-size: 21px;
    line-height: 33px;
    color: var(--ink-dark);
  }
</style>
</head>
<body>
  <section class="card card-front">
    <svg class="steel-panel" viewBox="0 0 612 382" aria-hidden="false">
      <defs>
        <linearGradient id="corrugated-tone" x1="0" y1="0" x2="1" y2="0">
          <stop offset="0" stop-color="#55585c"/>
          <stop offset="0.5" stop-color="#a9acb0"/>
          <stop offset="1" stop-color="#6b6e72"/>
        </linearGradient>
      </defs>
      <polygon points="340,36 383,0 612,0 612,189" fill="none" stroke="#9a9a9a" stroke-width="3"/>
      <polygon role="img" aria-label="Corrugated metal sheet panel" points="346,37 385,4 608,4 608,182" fill="url(#corrugated-tone)"/>
    </svg>
    <div class="front-name">RK<br>Ironcraft</div>
    <ul class="contact-list">
      <li class="contact-item phone">
        <svg class="contact-icon" viewBox="0 0 32 32">
          <circle cx="16" cy="16" r="15" fill="var(--icon-fill)"/>
          <path d="M10.5 8.5c1-.8 2-.6 2.6.3l1.6 2.5c.5.8.3 1.6-.4 2.1l-1 .8c.8 2 2.5 3.8 4.5 4.7l.8-1c.6-.7 1.4-.8 2.1-.3l2.5 1.7c.9.6 1 1.6.2 2.5l-1.2 1.3c-1 1-2.6 1.2-4.2.5-4.2-1.9-7.2-5-9-9.1-.7-1.6-.4-3.2.6-4.2z" fill="#2a2a2a"/>
        </svg>
        416-555-0193
      </li>
      <li class="contact-item email">
        <svg class="contact-icon" viewBox="0 0 32 32">
          <rect x="1" y="7" width="30" height="19" fill="var(--icon-fill)"/>
          <path d="M1 7l15 11L31 7M1 26l11-9M31 26l-11-9" fill="none" stroke="#2a2a2a" stroke-width="2"/>
        </svg>
        rk.ironcraftt@veltrano.com
      </li>
      <li class="contact-item social">
        <svg class="contact-icon" viewBox="0 0 32 32">
          <circle cx="16" cy="16" r="15" fill="var(--icon-fill)"/>
        </svg>
        rk_ironcraft_
      </li>
    </ul>
  </section>

  <section class="card card-back">
    <div class="back-name">RK<br>Ironcraft</div>
    <p class="service-list">
      Siding | ACM Panels | Standing Seam |<br>
      Soffit | Fascia, Gutters | Metal | Alumunium |<br>
      Vinyl | Metal Roof &amp; Roofing Repairs
    </p>
  </section>
</body>
</html>
```